Business Card Design For Tidecrest Audio

Tidecrest Audio is a small pro-audio company providing rental and install services for professional sound reinforcement. Focus is gigs (any gigs) needing high quality audio; from corporate to chamber music to hard hitting rock.

Tidecrest Audio
Pro-sound for every stage ... spine tingling
Doran Pelley
doran@tidecrestaudio.example.com.au
0482 356 071

We need a business card design and an "drop-off"' larger card (eg. one third A4 size: 99mm wide x 210mm high) with more details.
Updates

Please note I've had limited internet access for last few days and for the next four.  The work so far looks great .. I'll provide some individual feedback on the designs now.  Great work, many thanks, love the creativity!

Doran

Industry/Entity Type

Business

```html
<!DOCTYPE html>
<html lang="en">
<head>
<meta charset="utf-8">
<title>Tidecrest Audio – Business Card</title>
<link rel="stylesheet" href="https://fonts.googleapis.com/css2?family=Arimo:wght@400;700&display=swap">
<style>
  :root {
    --backdrop: #2b2b2d;
    --parchment-light: #f6eccb;
    --parchment-mid: #ecd9a3;
    --grunge-gold: #c99a3c;
    --grunge-brown: #7a4d15;
    --grunge-dark: #4a2c0b;
    --ink: #111111;
    --clef-gold: #b08a3e;
    --clef-brown: #6b3f1f;
  }
  * { margin: 0; padding: 0; box-sizing: border-box; }
  html, body {
    width: 1200px;
    height: 799px;
    overflow: hidden;
    background: var(--backdrop);
  }
  .canvas {
    position: relative;
    width: 1200px;
    height: 799px;
    display: flex;
    align-items: center;
    justify-content: center;
  }
  .business-card {
    position: relative;
    width: 1000px;
    height: 600px;
    overflow: hidden;
    font-family: "Arimo", Arial, sans-serif;
    color: var(--ink);
  }
  .card-texture {
    position: absolute;
    inset: 0;
    background:
      radial-gradient(ellipse 70% 62% at 50% 48%, var(--parchment-light) 0%, var(--parchment-light) 45%, var(--parchment-mid) 68%, var(--grunge-gold) 86%, var(--grunge-brown) 96%, var(--grunge-dark) 100%);
  }
  .card-content {
    position: absolute;
    inset: 0;
  }
  .brand-name {
    position: absolute;
    top: 52px;
    left: 0;
    right: 0;
    text-align: center;
    font-weight: 700;
    font-size: 64px;
    line-height: 1;
    letter-spacing: -0.5px;
  }
  .brand-name .initial {
    font-size: 96px;
    vertical-align: -6px;
  }
  .owner-name {
    position: absolute;
    top: 150px;
    left: 0;
    right: 0;
    text-align: center;
    font-size: 34px;
  }
  .tagline {
    position: absolute;
    top: 200px;
    left: 0;
    right: 0;
    text-align: center;
    font-weight: 700;
    font-size: 36px;
  }
  .contact {
    position: absolute;
    left: 40px;
    top: 370px;
    font-style: normal;
    font-weight: 700;
    font-size: 34px;
    line-height: 1.12;
  }
  .contact .contact-email {
    font-weight: 400;
    font-size: 33px;
  }
  .clef-ornament {
    position: absolute;
    right: 36px;
    bottom: 22px;
    width: 140px;
    height: 250px;
    border-radius: 60px 60px 40px 40px;
    background: linear-gradient(160deg, var(--clef-gold), var(--clef-brown));
    opacity: 0.85;
  }
</style>
</head>
<body>
  <main class="canvas">
    <article class="business-card">
      <div class="card-texture" role="img" aria-label="Aged parchment texture with weathered golden-brown grunge edges"></div>
      <div class="card-content">
        <h1 class="brand-name"><span class="initial">T</span>idecrest Audio</h1>
        <p class="owner-name">Doran Pelley</p>
        <p class="tagline">Pro-sound for every stage ... spine tingling</p>
        <address class="contact">
          <span class="contact-label">Contact us:-</span><br>
          <span class="contact-phone">0482 356 071</span><br>
          <span class="contact-email">doran@tidecrestaudio.example.com.au</span>
        </address>
        <div class="clef-ornament" role="img" aria-label="Metallic gold and brown treble clef ornament"></div>
      </div>
    </article>
  </main>
</body>
</html>
```